PLM - Business Card Design Project

We need a business card based on our logo
Updates

Hi I just upload logo file in AI format Thanks and regards

Target Market(s)

Bank, Big companies, Business owners

Industry/Entity Type

Business

Font styles to use
Sans Serif

```html
<!DOCTYPE html>
<html lang="en">
<head>
<meta charset="utf-8">
<title>PLM – Business Card</title>
<link rel="stylesheet" href="https://fonts.googleapis.com/css2?family=Open+Sans:wght@300;400;600&family=Arimo:wght@400&display=swap">
<style>
  :root {
    --backdrop: #1e1e1e;
    --card: #ffffff;
    --navy: #1c2e4e;
    --slate: #869694;
    --muted: #8a8f94;
  }
  * { margin: 0; padding: 0; box-sizing: border-box; }
  html, body {
    width: 1200px; height: 927px; overflow: hidden;
    background: var(--backdrop);
  }
  .card {
    position: absolute; left: 263px; top: 241px;
    width: 679px; height: 387px;
    background: var(--card);
    border-radius: 30px;
  }
  .logo-name {
    position: absolute; left: 0; width: 100%; top: 62px;
    text-align: center;
    font-family: "Open Sans", sans-serif; font-weight: 300;
    font-size: 128px; line-height: 1; letter-spacing: 2px;
    color: var(--navy);
  }
  .firm-name {
    position: absolute; left: 0; width: 100%; top: 190px;
    text-align: center;
    font-family: "Arimo", sans-serif; font-size: 22px;
    color: var(--navy);
  }
  .firm-services {
    position: absolute; left: 0; width: 100%; top: 217px;
    text-align: center;
    font-family: "Open Sans", sans-serif; font-size: 10px;
    color: var(--muted);
  }
  .person {
    position: absolute; right: 356px; top: 279px;
    text-align: right;
    font-family: "Open Sans", sans-serif; font-weight: 300;
  }
  .person-name { font-size: 33px; line-height: 1; letter-spacing: 0.5px; }
  .person-name .first { color: var(--navy); }
  .person-name .last { color: var(--slate); }
  .person-role {
    font-size: 17px; line-height: 1; margin-top: 8px;
    color: var(--slate); letter-spacing: 0.5px;
  }
  .divider {
    position: absolute; left: 328px; top: 286px;
    width: 15px; height: 51px; background: var(--slate);
  }
  .contact {
    position: absolute; left: 351px; top: 284px;
    list-style: none;
    font-family: "Open Sans", sans-serif; font-size: 15px;
    color: var(--slate);
  }
  .contact li { display: flex; align-items: center; height: 19.5px; }
  .contact svg { width: 11px; height: 11px; margin-right: 6px; fill: var(--navy); }
</style>
</head>
<body>
  <main class="card">
    <div class="logo-name">PLM</div>
    <div class="firm-name">Cabinet Morel &amp; Partenaires</div>
    <div class="firm-services">Expertise-comptable • Audit • Conseil</div>

    <div class="person">
      <div class="person-name"><span class="first">ADRIEN</span> <span class="last">TAN</span></div>
      <div class="person-role">DIRECTOR</div>
    </div>
    <div class="divider"></div>

    <ul class="contact">
      <li>
        <svg viewBox="0 0 12 12" aria-hidden="true"><path d="M1 4 Q6 0 11 4 L9.5 5.5 L8 4.5 L8 3.5 Q6 3 4 3.5 L4 4.5 L2.5 5.5 Z M3 6 H9 L10 11 H2 Z"/></svg>
        +65 9000 4417
      </li>
      <li>
        <svg viewBox="0 0 12 12" aria-hidden="true"><path d="M1 3 H11 V10 H1 Z" /><path d="M1 3 L6 7 L11 3" stroke="#fff" stroke-width="1" fill="none"/></svg>
        info@cabinetmorel.com
      </li>
      <li>
        <svg viewBox="0 0 12 12" aria-hidden="true"><circle cx="6" cy="6" r="5"/><path d="M1 6 H11 M6 1 V11 M6 1 Q3 6 6 11 M6 1 Q9 6 6 11" stroke="#fff" stroke-width="0.7" fill="none"/></svg>
        www.cabinetmorel.com
      </li>
    </ul>
  </main>
</body>
</html>
```